Flyer-Design für 3D Art aus Blech/Metall
Zielgruppe
3D Art aus Blech/Metall
Individuelles Design auf Kundenwunsch
Aufgabenstellung
Informationen anhand Vorlage im Anhang.
Flyer im Format A5 hoch oder quer
Hochwertiges & modernes Erscheinungsbild
Bilder von der Webseite nehmen www.vetrani.ch

```html
<!DOCTYPE html>
<html lang="de">
<head>
<meta charset="utf-8">
<title>Design &amp; Art by vetrani.ch – Flyer</title>
<link rel="stylesheet" href="https://fonts.googleapis.com/css2?family=Inter:wght@400;500&display=swap">
<style>
  :root {
    --backdrop: #bdbbba;
    --paper: #f3f3f3;
    --ink: #2b2b2b;
    --ink-soft: #4a4a4a;
    --accent-dark: #2e2e2e;
    --rust: #b4562a;
    --leaf: #6e8a3c;
    --night: #2b2e36;
    --wood: #cdb594;
    --slate: #3a3d44;
  }
  * { margin: 0; padding: 0; box-sizing: border-box; }
  html, body {
    width: 1200px; height: 864px; overflow: hidden;
    background: var(--backdrop);
    font-family: "Inter", Arial, sans-serif;
    color: var(--ink);
  }
  .flyer {
    position: absolute; left: 320px; top: 36px;
    width: 560px; height: 792px;
    background: var(--paper);
    box-shadow: 0 10px 30px rgba(0,0,0,.25);
  }
  .brand {
    position: absolute; left: 70px; top: 58px;
    display: flex; flex-direction: column; align-items: center; gap: 8px;
  }
  .brand-dot {
    width: 58px; height: 58px; border-radius: 50%;
    border: 2.5px solid var(--ink);
  }
  .brand-name { font-size: 15px; font-weight: 500; }
  .photo { position: absolute; }
  .photo-interior { left: 224px; top: 88px; width: 160px; height: 144px;
    background: linear-gradient(160deg, var(--night), #4a4c55 60%, #6b5a4e); }
  .photo-sign { left: 392px; top: 44px; width: 123px; height: 188px;
    background: linear-gradient(180deg, var(--wood) 0 62%, var(--slate) 62%); }
  .photo-planter { left: 224px; top: 240px; width: 291px; height: 246px;
    background: linear-gradient(170deg, #dfe2e3 0 18%, var(--leaf) 18% 40%, var(--rust) 40% 88%, #c9c8c4 88%); }
  .mark-square { position: absolute; width: 20px; height: 20px; background: var(--accent-dark); }
  .mark-left { left: 0; top: 580px; }
  .mark-right { right: 0; top: 702px; }
  .headline {
    position: absolute; left: 84px; top: 560px;
    font-size: 44px; font-weight: 500; line-height: 1.08; letter-spacing: -0.5px;
  }
  .tagline {
    position: absolute; left: 86px; top: 670px;
    font-size: 16px; font-weight: 400; letter-spacing: 1.6px; text-transform: uppercase;
    color: var(--ink-soft);
  }
  .rule { position: absolute; left: 106px; right: 30px; top: 728px; height: 1px; background: var(--ink); }
  .contact {
    position: absolute; left: 106px; top: 742px;
    font-size: 10px; color: var(--ink-soft); letter-spacing: .2px;
  }
</style>
</head>
<body>
  <main class="flyer">
    <div class="brand">
      <span class="brand-dot"></span>
      <span class="brand-name">vetrani.ch</span>
    </div>

    <div class="photo photo-interior" role="img" aria-label="Restaurant-Innenraum mit Rost-Blechbildern an dunkler Wand und Lichterkette"></div>
    <div class="photo photo-sign" role="img" aria-label="Schwarzes Blechschild an Holzwand über Steinmauer"></div>
    <div class="photo photo-planter" role="img" aria-label="Rostiger Pflanzkasten mit ausgeschnittenem Motiv und Bambus"></div>

    <span class="mark-square mark-left"></span>
    <span class="mark-square mark-right"></span>

    <h1 class="headline">Design &amp; Art<br>by vetrani.ch</h1>
    <p class="tagline">Blechdesign aus Seefeldau</p>

    <div class="rule"></div>
    <p class="contact">Lukas Brunner | 079 481 62 30 | lbrunner@mailbox.ch | vetrani.ch</p>
  </main>
</body>
</html>
```